New boutique hotel for tourists, with hint of art deco styling

This is a new, soon to be completed, boutique hotel in Sydney. A letterhead with a logo is required. Less emphasis on the word "boutique". Perhaps the word could be screened to be lighter in colour (or print intensity). Would like a simple, clear, easy-to read, sans serif type face. The information on the letterhead is:
Mrs Perrow Boutique Hotel
418 Calloway Street,
Wrenfield, NSW, 2094
Australia
Tel: +61 2 9478-0000
mrsperrowhotel@example-mail.com
mrsperrowhotel.com.au
ABN 47 902 365 118

Target Market(s)

travellers, tourists, various ages

Industry/Entity Type

Hospitality

Contact Information for Business Card

Mrs Perrow Boutique Hotel
418 Calloway Street,
Wrenfield, NSW, 2094
Telephone: (02) 9478-0000
www.mrsperrowhotel.com.au
mrsperrowhotel@example-mail.com
ABN 47 902 365 118

Logo Text

suggest playing with the letter "B"

Font styles to use
Sans Serif

Colors
3176b5

Requirements
Must have
• ABN to be very small.
• Must be clear, easy to read and in a sans serif typeface, please!
Nice to have
• The word "Boutique" should be less intense in appearance to the rest of the name, or even "Boutique Hotel" can have less prominence than "Mrs Perrow".
Should not have
• No serif typeface. Sans serif only will be accepted.

```html
<!DOCTYPE html>
<html lang="en">
<head>
<meta charset="utf-8">
<title>Mrs Perrow Boutique Hotel — Letterhead</title>
<link rel="stylesheet" href="https://fonts.googleapis.com/css2?family=Quicksand:wght@400;500;600&display=swap">
<style>
  :root {
    --brand-blue: #3176b5;
    --band-blue: #2c77b8;
    --paper: #ffffff;
    --faint: #f1f4f8;
    --on-band: #ffffff;
    --on-band-soft: #dce8f4;
  }
  * { margin: 0; padding: 0; box-sizing: border-box; }
  html, body {
    width: 848px;
    height: 1200px;
    overflow: hidden;
    background: var(--paper);
  }
  body {
    font-family: "Quicksand", sans-serif;
    color: var(--brand-blue);
  }
  .letterhead {
    position: relative;
    width: 848px;
    height: 1200px;
    background: var(--paper);
    overflow: hidden;
  }
  .masthead {
    position: absolute;
    top: 52px;
    left: 0;
    width: 100%;
    text-align: center;
  }
  .masthead__dot {
    display: block;
    width: 52px;
    height: 52px;
    margin: 0 auto 16px;
    border-radius: 50%;
    background: var(--brand-blue);
  }
  .masthead__name {
    font-size: 46px;
    font-weight: 500;
    line-height: 1;
    letter-spacing: -0.5px;
    color: var(--brand-blue);
  }
  .masthead__tagline {
    margin-top: 10px;
    font-size: 18px;
    font-weight: 500;
    letter-spacing: 1.6px;
    color: var(--brand-blue);
    opacity: 0.85;
  }
  .backdrop-disc {
    position: absolute;
    left: 246px;
    top: 378px;
    width: 356px;
    height: 356px;
    border-radius: 50%;
    background: var(--faint);
  }
  .footer-band {
    position: absolute;
    left: 0;
    top: 997px;
    width: 848px;
    height: 203px;
    background: var(--band-blue);
    color: var(--on-band);
  }
  .footer-band__name {
    position: absolute;
    left: 31px;
    top: 20px;
    font-size: 34px;
    font-weight: 500;
    letter-spacing: -0.5px;
    line-height: 1;
  }
  .contact-list,
  .address {
    position: absolute;
    list-style: none;
    font-size: 20px;
    font-weight: 500;
    line-height: 29px;
    white-space: nowrap;
  }
  .contact-list { left: 31px; top: 72px; }
  .address { left: 400px; top: 79px; font-style: normal; }
  .abn {
    position: absolute;
    left: 662px;
    top: 144px;
    font-size: 13px;
    font-weight: 500;
    color: var(--on-band-soft);
    white-space: nowrap;
  }
</style>
</head>
<body>
  <main class="letterhead">
    <header class="masthead">
      <span class="masthead__dot" aria-hidden="true"></span>
      <div class="masthead__name">Mrs Perrow</div>
      <div class="masthead__tagline">BOUTIQUE HOTEL</div>
    </header>

    <div class="backdrop-disc" aria-hidden="true"></div>

    <footer class="footer-band">
      <div class="footer-band__name">Mrs Perrow</div>
      <ul class="contact-list">
        <li>mrsperrowhotel@example-mail.com</li>
        <li>mrsperrowhotel.com.au</li>
        <li>Tel: +61 2 9478-0000</li>
      </ul>
      <address class="address">
        418 Calloway Street<br>
        Wrenfield, NSW, 2094<br>
        Australia
      </address>
      <div class="abn">ABN 47 902 365 118</div>
    </footer>
  </main>
</body>
</html>
```